Tallowmere Capital Partners- Business Card

We need a professional business card that conveys confidence and trust. Strength. A modern and still yet, traditional financial planner/advisor format. I will upload a logo file or two, you do not have to use it, if it does not work for the design.

Target Market(s)

high net worth

Industry/Entity Type

Finance

Contact Information for Business Card

Address: 24836 Orchard Ave. Suite 400, Huntington Beach, CA 93518, website: tallowmerecap.example, ph # (555) 271-6094, email address: rpoulsen@tallowmerecap.example

```html
<!DOCTYPE html>
<html lang="en">
<head>
<meta charset="utf-8">
<title>Tallowmere Capital Partners – Business Card</title>
<link rel="stylesheet" href="https://fonts.googleapis.com/css2?family=Playfair+Display:wght@400&family=Arimo:wght@400;700&display=swap">
<style>
  :root {
    --navy: #0b2a6e;
    --navy-deep: #06235f;
    --gold: #b8923a;
    --ink: #1d1d1d;
    --paper: #ffffff;
    --backdrop: #e9e7e3;
  }
  * { box-sizing: border-box; margin: 0; padding: 0; }
  html, body { width: 1200px; height: 977px; overflow: hidden; background: var(--backdrop); }
  .canvas { position: relative; width: 1200px; height: 977px; }

  .card {
    position: absolute;
    width: 600px; height: 343px;
    border-radius: 22px;
    box-shadow: 0 10px 28px rgba(0,0,0,.18);
    overflow: hidden;
  }

  /* Front */
  .card-front { left: 60px; top: 90px; background: var(--navy-deep); }
  .front-brand {
    position: absolute; left: 0; right: 0; top: 50%;
    transform: translateY(-50%);
    display: flex; align-items: center; justify-content: center; gap: 16px;
    white-space: nowrap;
  }
  .brand-square {
    width: 38px; height: 38px; flex: none;
    border: 2px solid var(--gold);
  }
  .front-name {
    font-family: "Playfair Display", serif;
    font-weight: 400;
    font-variant: small-caps;
    font-size: 29px;
    letter-spacing: .3px;
    color: var(--paper);
  }

  /* Back */
  .card-back { left: 540px; top: 540px; background: var(--paper); font-family: "Arimo", sans-serif; }
  .back-mark {
    position: absolute; right: 62px; top: 30px;
    width: 112px; height: 112px;
    border: 3px solid var(--gold);
  }
  .person { position: absolute; left: 40px; top: 108px; }
  .person-name {
    font-weight: 700; font-size: 34px; color: var(--navy); letter-spacing: .5px;
  }
  .person-title { font-size: 20px; color: var(--gold); margin-top: 2px; }
  .divider {
    position: absolute; left: 40px; right: 40px; top: 186px;
    height: 2px; background: var(--navy);
  }
  .contacts {
    position: absolute; left: 40px; top: 202px;
    list-style: none; font-size: 16px; color: var(--ink); line-height: 27px;
    white-space: nowrap;
  }
  .contacts li { display: flex; align-items: center; gap: 10px; }
  .contacts svg { width: 15px; height: 15px; fill: var(--gold); flex: none; }
  .company {
    position: absolute; right: 40px; top: 204px;
    text-align: right; font-size: 14px; line-height: 22px; color: var(--ink);
    font-style: normal; white-space: nowrap;
  }
  .company-name { font-weight: 700; color: var(--gold); font-size: 15px; }
</style>
</head>
<body>
<main class="canvas">

  <section class="card card-front" aria-label="Card front">
    <div class="front-brand">
      <span class="brand-square" aria-hidden="true"></span>
      <span class="front-name">Tallowmere Capital Partners</span>
    </div>
  </section>

  <section class="card card-back" aria-label="Card back">
    <span class="back-mark" aria-hidden="true"></span>

    <div class="person">
      <p class="person-name">RHEA POULSEN</p>
      <p class="person-title">Creative Director</p>
    </div>

    <div class="divider"></div>

    <ul class="contacts">
      <li>
        <svg viewBox="0 0 16 16" aria-hidden="true"><path d="M3.6 1.5l2.3 2.6-1.3 1.6c.9 2 2.5 3.6 4.6 4.6l1.6-1.3 2.6 2.3-1.2 2.2C7.5 15 1 8.5 1.4 2.7z"/></svg>
        (555) 271-6094
      </li>
      <li>
        <svg viewBox="0 0 16 16" aria-hidden="true"><path d="M4.5 1h7a1 1 0 0 1 1 1v12a1 1 0 0 1-1 1h-7a1 1 0 0 1-1-1V2a1 1 0 0 1 1-1zm.5 2v9h6V3zm3 10a.8.8 0 1 0 0 1.6.8.8 0 0 0 0-1.6z"/></svg>
        (555) 271-6094
      </li>
      <li>
        <svg viewBox="0 0 16 16" aria-hidden="true"><path d="M4 1h8v4H4zM1.5 6h13a1 1 0 0 1 1 1v5h-3v3h-9v-3h-3V7a1 1 0 0 1 1-1zm3 5v3h7v-3z"/></svg>
        (555) 271-6094
      </li>
      <li>
        <svg viewBox="0 0 16 16" aria-hidden="true"><path d="M1 3h14v1.2L8 9 1 4.2zm0 2.6l7 4.8 7-4.8V13H1z"/></svg>
        rpoulsen@tallowmerecap.example
      </li>
    </ul>

    <address class="company">
      <p class="company-name">Tallowmere Capital Partners</p>
      <p>24836 Orchard Ave. Suite 400</p>
      <p>Huntington Beach, CA 93518</p>
      <p>www.tallowmerecap.example</p>
    </address>
  </section>

</main>
</body>
</html>
```